facelift of our car wrap design - for Varno Kestel L2

We would like to give our vehicles a facelift. Attached is our current advertising material.
Must-have: The paintwork of our vehicles is and will remain yellow. I would prefer to use the newer company logo, without the coloured bars, as shown in the attachment.
You can find further inspiration at www.blumaaaak.ch.

Target Market(s)

it should be a classic new design

Requirements
Nice to have
• some advertising keywords

```html
<!DOCTYPE html>
<html lang="de">
<head>
<meta charset="utf-8">
<title>Blumaaaak – Fahrzeugbeschriftung Varno Kestel L2</title>
<link rel="stylesheet" href="https://fonts.googleapis.com/css2?family=Jost:wght@400;600&display=swap">
<style>
  :root {
    --paint-yellow: #f4d31a;
    --paint-shade: #e2c00f;
    --wrap-black: #1a1a1a;
    --trim-grey: #2e2e2e;
    --glass: #8f979b;
    --backdrop: #ececec;
    --floor: #e4e4e4;
  }
  html, body {
    margin: 0;
    width: 1200px;
    height: 1200px;
    overflow: hidden;
    background: var(--backdrop);
  }
  .canvas {
    position: relative;
    width: 1200px;
    height: 1200px;
    background: linear-gradient(#f2f2f2 0%, #e6e6e6 70%, var(--floor) 70.6%, var(--floor) 100%);
  }
  .vehicle-side {
    position: absolute;
    left: 0;
    top: 0;
    width: 1200px;
    height: 1200px;
  }
  .brand-name {
    font-family: "Jost", sans-serif;
    font-weight: 600;
    font-size: 50px;
    letter-spacing: 2px;
    fill: var(--wrap-black);
  }
  .brand-tagline {
    font-family: "Jost", sans-serif;
    font-weight: 400;
    font-size: 17px;
    letter-spacing: 2.2px;
    fill: var(--wrap-black);
  }
  .contact-phone {
    font-family: "Jost", sans-serif;
    font-weight: 400;
    font-size: 16px;
    letter-spacing: 1.4px;
    fill: var(--wrap-black);
  }
</style>
</head>
<body>
<main class="canvas">
  <svg class="vehicle-side" viewBox="0 0 960 960" xmlns="http://www.w3.org/2000/svg" aria-label="Seitenansicht der gelben Fahrzeugbeschriftung">
    <!-- body -->
    <path class="body-panel" fill="var(--paint-yellow)"
      d="M58 325 Q60 318 80 317 L575 316 Q620 318 660 345 L770 430 Q800 462 855 490
         Q895 505 903 560 L905 640 L832 645 A52 52 0 0 0 728 645 L285 648 A52 52 0 0 0 180 648
         L60 640 L52 620 Z"/>
    <!-- roof seam and panel lines -->
    <path d="M80 377 L582 377" stroke="var(--paint-shade)" stroke-width="1.5" fill="none"/>
    <path d="M98 383 L548 383 Q556 383 556 391 L556 490" stroke="var(--paint-shade)" stroke-width="1.2" fill="none"/>
    <path d="M584 378 L584 648 M718 420 L718 648" stroke="#c9aa0c" stroke-width="1.2" fill="none"/>
    <!-- rear light -->
    <rect x="52" y="498" width="22" height="86" fill="#c8282d"/>
    <rect x="52" y="540" width="22" height="8" fill="#f0f0f0"/>
    <!-- side windows -->
    <path d="M596 388 L672 388 Q680 388 688 396 L730 440 L730 500 L604 488 Q596 487 596 478 Z" fill="var(--glass)"/>
    <!-- lower trim band -->
    <path d="M75 588 L840 588 L840 615 L75 615 Z" fill="var(--trim-grey)"/>
    <path d="M52 592 L90 592 L90 640 L52 640 Z" fill="var(--trim-grey)"/>
    <path d="M832 580 Q880 580 905 590 L905 640 L832 645 Z" fill="var(--trim-grey)"/>
    <!-- headlight -->
    <path d="M852 532 L892 530 Q900 545 898 572 L862 556 Z" fill="#d9dde0"/>
    <!-- wheels -->
    <g class="wheel">
      <circle cx="232" cy="640" r="50" fill="var(--wrap-black)"/>
      <circle cx="232" cy="640" r="30" fill="#b9bcbe"/>
      <circle cx="232" cy="640" r="9" fill="#6b6e70"/>
    </g>
    <g class="wheel">
      <circle cx="780" cy="640" r="50" fill="var(--wrap-black)"/>
      <circle cx="780" cy="640" r="30" fill="#b9bcbe"/>
      <circle cx="780" cy="640" r="9" fill="#6b6e70"/>
    </g>
    <!-- door handles -->
    <rect x="528" y="513" width="38" height="5" rx="2.5" fill="var(--wrap-black)"/>
    <rect x="593" y="513" width="38" height="5" rx="2.5" fill="var(--wrap-black)"/>

    <!-- wrap graphics -->
    <path class="swoosh" d="M75 507 L700 549 L75 540 Z" fill="var(--wrap-black)"/>
    <rect class="rule" x="98" y="488" width="214" height="6" fill="var(--trim-grey)"/>

    <text class="brand-name" x="136" y="442">BLUMAAAAK</text>
    <text class="brand-tagline" x="138" y="474">HAUSTECHNIK + BAUSPENGLEREI</text>
    <text class="contact-phone" x="334" y="519">T +41 44 318 72 40</text>
  </svg>
</main>
</body>
</html>
```